CREATE R&B MIXTAPE COVER !!
Hi , my name is Brontel , and I want you to create a cover for my music mixtape.
The name of the mixtape is Tormenta , and has these types of music :
- R&B
- Hiphop
- Afrohouse
- Dancehall
- Reggaeton
In the attachments you’ll find two backgrounds. One with a lightning bolt , and a grey one with a stroke in the middle. I like both very much , but don’t know which one to choose. That’s why I want to compare the end results of both , and then make a decision. Below you’ll find instructions for both backgrounds.
If you think you can make something better for me , you can also try to do your own thing , and use your own background for example.
Instructions for the first background ( Lightning bolt )
I would like you to design my name ‘Brontel’ into / onto the lightning bolt. I want the lightning bolt + my name to be my DJ Logo , but my name doesn’t have to be in very big letters. Tormenta is the name of the mixtape and has to be in big letters. I was thinking above the logo.
Then there are 2 remaining sentences : ‘Mixed by DJ Brontel’ and ‘Mixtape Volume 1’. These two sentences have to be smaller than ‘Tormenta’. You can put them under the logo.
Instructions for the second background ( Grey )
I would like you to create a logo of my whole name ‘Brontel’ Or just with the letter V. You can put the logo above the stroke.
The mixtape name ‘Tormenta’ has to be in the middle in big letters.
Then there are 2 remaining sentences : ‘Mixed by DJ Brontel’ and ‘Mixtape Volume 1’. These two have to be smaller than ‘Tormenta’ in the middle. I want these sentences below.
Use your imagination with the name Tormenta , the two sentences and the logo. I want it to look professional and unique.
Kind regards ,
Brontel

```html
<!DOCTYPE html>
<html lang="en">
<head>
<meta charset="utf-8">
<title>Tormenta – Mixtape Volume 1</title>
<link rel="stylesheet" href="https://fonts.googleapis.com/css2?family=Rubik+Dirt&family=Tinos&display=swap">
<style>
  :root {
    --night: #0b1520;
    --night-deep: #060b10;
    --dusk-red: #8a3a1c;
    --sun-orange: #f5921e;
    --sun-gold: #ffd23a;
    --horizon: #050505;
    --sea-green: #3f8f1c;
    --sea-bright: #9bd22a;
    --sea-deep: #0d2a12;
    --title-green: #8fd12a;
    --title-yellow: #e6d22a;
    --title-orange: #e2521c;
    --mark: #120c06;
    --caption: #1a2410;
  }
  html, body {
    margin: 0;
    padding: 0;
    overflow: hidden;
    background: var(--night-deep);
  }
  .cover {
    position: relative;
    width: 1200px;
    height: 1200px;
    overflow: hidden;
  }
  .cover__scene {
    position: absolute;
    inset: 0;
    background:
      radial-gradient(ellipse 320px 70px at 640px 462px, rgba(255,230,120,0.95), rgba(255,160,40,0) 70%),
      radial-gradient(ellipse 900px 260px at 640px 860px, rgba(190,240,60,0.75), rgba(60,140,30,0) 70%),
      linear-gradient(180deg,
        var(--night) 0%,
        var(--night) 12%,
        var(--dusk-red) 19%,
        var(--sun-orange) 25%,
        var(--sun-orange) 31%,
        var(--sun-gold) 36%,
        var(--sun-orange) 38.5%,
        var(--horizon) 39%,
        var(--horizon) 58%,
        var(--sea-green) 64%,
        var(--sea-bright) 71%,
        var(--sea-green) 80%,
        var(--sea-deep) 92%,
        var(--night-deep) 100%);
  }
  .brand-mark {
    position: absolute;
    top: 270px;
    left: 0;
    width: 1200px;
    display: flex;
    justify-content: center;
    align-items: center;
    gap: 22px;
  }
  .brand-mark__dot {
    width: 70px;
    height: 70px;
    border: 9px solid var(--mark);
    border-radius: 50%;
    box-sizing: border-box;
  }
  .brand-mark__name {
    font-family: "Rubik Dirt", sans-serif;
    font-size: 88px;
    color: var(--mark);
    line-height: 1;
  }
  .title {
    position: absolute;
    top: 450px;
    left: 0;
    width: 1200px;
    margin: 0;
    text-align: center;
    white-space: nowrap;
    font-family: "Rubik Dirt", sans-serif;
    font-weight: 400;
    font-size: 212px;
    line-height: 1.1;
    letter-spacing: 0;
    background: linear-gradient(90deg, var(--title-green) 0%, var(--title-green) 35%, var(--title-yellow) 62%, var(--title-orange) 100%);
    -webkit-background-clip: text;
    background-clip: text;
    color: transparent;
  }
  .caption {
    position: absolute;
    top: 792px;
    left: 0;
    width: 1200px;
    margin: 0;
    text-align: center;
    font-family: "Tinos", serif;
    font-size: 25px;
    color: var(--caption);
  }
</style>
</head>
<body>
  <main class="cover">
    <div class="cover__scene" role="img" aria-label="Photograph of a sunset over the horizon with a glowing orange sky above and a green reflected sea below"></div>

    <div class="brand-mark">
      <span class="brand-mark__dot"></span>
      <span class="brand-mark__name">Brontel</span>
    </div>

    <h1 class="title">Tormenta</h1>

    <p class="caption">Mixtape Volume 1 - Mixed by DJ Brontel</p>
  </main>
</body>
</html>
```